Christmas Collection Candle Label Design

Looking to update our existing Christmas Candle Collection labels. Labels should reflect the overall feel of our brand- www.kelvabrite.ca
Want to include some color elements. Holiday colors added into design but more muted/ earthy tones not vibrant colors . Metallic elements and line art botanical illustration. Fonts should be more align to brand
Scents
Winter Lantern
Frost Berry
Amber and Fig
Belle Étoile

```html
<!DOCTYPE html>
<html lang="en">
<head>
<meta charset="utf-8">
<title>Christmas Collection Candle Labels</title>
<link rel="stylesheet" href="https://fonts.googleapis.com/css2?family=Bodoni+Moda:wght@500&family=Crimson+Pro:wght@400&family=Montserrat:wght@800&family=Sacramento&display=swap">
<style>
  :root {
    --backdrop: #c2bfb8;
    --backdrop-word: #c9c9c0;
    --cream: #fffdf1;
    --rule: #c9c6bd;
    --ink: #5a5753;
    --rust: #b96a4b;
    --rust-soft: #f7d3cf;
    --plum: #977596;
    --plum-soft: #ddbbd2;
    --taupe: #9b8a76;
    --taupe-soft: #dcd1c6;
    --sage: #879386;
    --sage-soft: #d3e3d9;
    --sprig: #ece3d8;
  }
  * { box-sizing: border-box; margin: 0; padding: 0; }
  html, body { width: 1200px; height: 935px; overflow: hidden; }
  body { background: var(--backdrop); position: relative; font-family: "Crimson Pro", serif; }

  .backdrop-word {
    position: absolute; left: 0; width: 1200px; text-align: center;
    font-family: "Montserrat", sans-serif; font-weight: 800;
    font-size: 192px; line-height: 1; letter-spacing: 2px;
    color: var(--backdrop-word);
  }
  .backdrop-word--top { top: 12px; left: 0; }
  .backdrop-word--bottom { top: 770px; }

  .label {
    position: absolute; width: 435px; height: 290px;
    box-shadow: 0 22px 30px rgba(60, 55, 50, 0.28);
  }
  .label--lantern { left: 114px; top: 131px; --accent: var(--rust); --accent-soft: var(--rust-soft); }
  .label--berry { left: 649px; top: 131px; --accent: var(--plum); --accent-soft: var(--plum-soft); }
  .label--fig { left: 114px; top: 515px; --accent: var(--taupe); --accent-soft: var(--taupe-soft); }
  .label--etoile { left: 649px; top: 515px; --accent: var(--sage); --accent-soft: var(--sage-soft); }

  .label__pattern {
    position: absolute; inset: 0;
    background: linear-gradient(115deg, var(--accent-soft) 0%, var(--accent) 45%, var(--accent-soft) 70%, var(--accent) 100%);
  }
  .label__panel {
    position: absolute; left: 21px; top: 21px; right: 21px; bottom: 21px;
    background: var(--cream);
  }
  .label__frame {
    position: absolute; left: 12px; top: 12px; right: 12px; bottom: 12px;
    border: 1px solid var(--rule);
  }
  .label__tagline {
    position: absolute; left: 0; right: 0; top: 22px; text-align: center;
    font-family: "Sacramento", cursive; font-size: 16px; letter-spacing: 4px;
    color: var(--ink);
  }
  .label__title {
    position: absolute; left: 0; right: 0; top: 76px; text-align: center;
    color: var(--accent); white-space: nowrap;
  }
  .label__title-main {
    font-family: "Bodoni Moda", serif; font-weight: 500; font-size: 36px;
    letter-spacing: -1px;
  }
  .label__title-script {
    font-family: "Sacramento", cursive; font-size: 40px;
    position: relative; top: 10px; margin-left: 2px;
  }
  .label__sprig {
    position: absolute; left: 134px; top: 140px; width: 121px; height: 47px;
    border-radius: 50%;
    background: radial-gradient(ellipse at center, var(--sprig) 0%, rgba(236, 227, 216, 0) 70%);
  }
  .label__facts {
    position: absolute; left: 0; right: 0; top: 204px; text-align: center;
    font-size: 11.5px; letter-spacing: 0.4px; color: var(--ink); white-space: nowrap;
  }
  .label__divider { color: var(--accent); margin: 0 11px; }
</style>
</head>
<body>
  <div class="backdrop-word backdrop-word--top">CANDLE</div>
  <div class="backdrop-word backdrop-word--bottom">LABEL</div>

  <article class="label label--lantern">
    <div class="label__pattern" role="img" aria-label="Rust and blush wavy stripe pattern border"></div>
    <div class="label__panel">
      <div class="label__frame"></div>
      <p class="label__tagline">made with plant based botanicals</p>
      <h2 class="label__title"><span class="label__title-main">WINTER</span><span class="label__title-script">Lantern</span></h2>
      <div class="label__sprig" role="img" aria-label="Faint line art botanical sprig"></div>
      <p class="label__facts">Net Wt. 25oz/709g<span class="label__divider">|</span>Made in Canada<span class="label__divider">|</span>Kelva Brite</p>
    </div>
  </article>

  <article class="label label--berry">
    <div class="label__pattern" role="img" aria-label="Plum and lilac wavy stripe pattern border"></div>
    <div class="label__panel">
      <div class="label__frame"></div>
      <p class="label__tagline">made with plant based botanicals</p>
      <h2 class="label__title"><span class="label__title-main">FROST</span><span class="label__title-script">Berry</span></h2>
      <div class="label__sprig" role="img" aria-label="Faint line art botanical sprig"></div>
      <p class="label__facts">Net Wt. 25oz/709g<span class="label__divider">|</span>Made in Canada<span class="label__divider">|</span>Kelva Brite</p>
    </div>
  </article>

  <article class="label label--fig">
    <div class="label__pattern" role="img" aria-label="Taupe and sand wavy stripe pattern border"></div>
    <div class="label__panel">
      <div class="label__frame"></div>
      <p class="label__tagline">made with plant based botanicals</p>
      <h2 class="label__title"><span class="label__title-main">AMBER</span><span class="label__title-script">&amp;Fig</span></h2>
      <div class="label__sprig" role="img" aria-label="Faint line art botanical sprig"></div>
      <p class="label__facts">Net Wt. 25oz/709g<span class="label__divider">|</span>Made in Canada<span class="label__divider">|</span>Kelva Brite</p>
    </div>
  </article>

  <article class="label label--etoile">
    <div class="label__pattern" role="img" aria-label="Sage and mint wavy stripe pattern border"></div>
    <div class="label__panel">
      <div class="label__frame"></div>
      <p class="label__tagline">made with plant based botanicals</p>
      <h2 class="label__title"><span class="label__title-main">BELLE</span><span class="label__title-script">Étoile</span></h2>
      <div class="label__sprig" role="img" aria-label="Faint line art botanical sprig"></div>
      <p class="label__facts">Net Wt. 25oz/709g<span class="label__divider">|</span>Made in Canada<span class="label__divider">|</span>Kelva Brite</p>
    </div>
  </article>
</body>
</html>
```